Business Card Design Project

New Business Card design for Varodine Technology Ltd using new Logo and new Tagline for staffing company.

About us from our website - www.varodine.example:

VaroDine is a leading and recognized Electronic Entertainment, Workforce Augmentation, and Project Management solutions provider with clients in Electronic Entertainment, Legal, Technology, Government and other verticals that range in size from start up organizations to Zenlar 500 companies. VaroDine is certified as an 8(a) minority and woman owned enterprise, established in 1998.

Target Market(s)

Companies in Electronic Entertainment, Legal, Government and Technology

Industry/Entity Type

Business

Requirements
Must have
• Must include in small letters the following information on back:

Established in 1998
8(a)(w)(e), Cage #7KRT9, DUNS #462137580

Front should have the following:
Derek Holloway
Vice President
5820 Birchmont Road
Fallowby, FB 482917
555-318-2746 X 100
555-902-6613 Fax
555-318-2746 Toll Free
name@varodine.example

Our Tagline: Connect • Collaborate • Achieve

```html
<!DOCTYPE html>
<html lang="en">
<head>
<meta charset="utf-8">
<title>VaroDine Business Card</title>
<link rel="stylesheet" href="https://fonts.googleapis.com/css2?family=Arimo:wght@400;700&display=swap">
<style>
  :root {
    --backdrop: #d6d6d6;
    --card-white: #ffffff;
    --brand-blue: #0a57a8;
    --brand-blue-deep: #123a8a;
    --brand-blue-light: #1f79c9;
    --ink-grey: #58595b;
    --text-grey: #555555;
    --fold-shadow: #1b1b1b;
  }
  * { margin: 0; padding: 0; box-sizing: border-box; }
  html, body {
    width: 1200px; height: 900px; overflow: hidden;
    background: var(--backdrop);
    font-family: "Arimo", Arial, sans-serif;
  }
  .canvas { position: relative; width: 1200px; height: 900px; }

  /* Back of card */
  .card-back {
    position: absolute; left: 190px; top: 438px;
    width: 528px; height: 330px; overflow: hidden;
    background: radial-gradient(circle at 45% 35%, var(--brand-blue-light) 0%, var(--brand-blue) 45%, var(--brand-blue-deep) 100%);
    box-shadow: 0 4px 10px rgba(0,0,0,0.25);
  }
  .card-back .facet { position: absolute; inset: 0; }
  .card-back .wordmark {
    position: absolute; left: 0; right: 0; top: 118px;
    display: flex; align-items: center; justify-content: center; gap: 12px;
    color: #fff; font-weight: 700; font-size: 50px; letter-spacing: -1px;
  }
  .card-back .wordmark .dot {
    width: 18px; height: 18px; border-radius: 50%; background: #fff;
  }
  .card-back .credentials {
    position: absolute; left: 0; right: 0; top: 256px;
    text-align: center; color: #fff; font-size: 14px; line-height: 18px;
  }

  /* Front of card */
  .card-front {
    position: absolute; left: 500px; top: 130px;
    width: 506px; height: 330px; overflow: hidden;
    background: var(--card-white);
    box-shadow: 0 5px 14px rgba(0,0,0,0.3);
  }
  .card-front .wordmark {
    position: absolute; left: 40px; top: 78px;
    display: flex; align-items: center; gap: 8px;
    color: var(--ink-grey); font-weight: 700; font-size: 36px; letter-spacing: -1px;
  }
  .card-front .wordmark .dot {
    width: 14px; height: 14px; border-radius: 50%; background: var(--brand-blue);
  }
  .tagline {
    position: absolute; left: 48px; width: 158px; top: 178px;
    text-align: center; color: var(--brand-blue);
    font-weight: 700; font-size: 16px; line-height: 24px; list-style: none;
  }
  .edge-shade {
    position: absolute; right: 0; top: 120px; width: 24px; height: 210px;
    background: linear-gradient(90deg, #ffffff 0%, #9c9c9c 100%);
  }
  .name-band {
    position: absolute; left: 278px; top: 65px; width: 222px; height: 57px;
    padding: 10px 0 0 20px; color: #fff;
    background: linear-gradient(90deg, var(--brand-blue-light) 0%, var(--brand-blue) 60%, var(--brand-blue-deep) 100%);
    box-shadow: 0 4px 6px rgba(0,0,0,0.35);
  }
  .name-band .person { font-weight: 700; font-size: 17px; letter-spacing: 0.3px; }
  .name-band .role { font-size: 14px; margin-top: 2px; }
  .corner-fold { position: absolute; right: 0; top: 0; }
  .contact {
    position: absolute; left: 275px; top: 150px;
    color: var(--text-grey); font-size: 14.5px; line-height: 20.5px; list-style: none;
  }
  .contact li { display: flex; align-items: center; gap: 5px; }
  .contact svg { width: 14px; height: 12px; fill: var(--brand-blue); flex: none; }
</style>
</head>
<body>
<div class="canvas">

  <section class="card-back" aria-label="Card back">
    <svg class="facet" viewBox="0 0 528 330" aria-hidden="true">
      <polygon points="220,0 528,0 528,330" fill="#1a3f8f" opacity="0.55"/>
      <polygon points="345,180 528,330 355,200" fill="#0b2a6a" opacity="0.6"/>
    </svg>
    <div class="wordmark"><span class="dot"></span><span>VaroDine</span></div>
    <p class="credentials">Established in 1998<br>8(a)(w)(e), Cage #7KRT9, DUNS #462137580</p>
  </section>

  <section class="card-front" aria-label="Card front">
    <div class="wordmark"><span>VaroDine</span><span class="dot"></span></div>
    <ul class="tagline">
      <li>Connect</li>
      <li>Collaborate</li>
      <li>Achieve</li>
    </ul>
    <div class="edge-shade"></div>
    <div class="name-band">
      <div class="person">DEREK HOLLOWAY</div>
      <div class="role">Vice President</div>
    </div>
    <svg class="corner-fold" width="32" height="70" viewBox="0 0 32 70" aria-hidden="true">
      <polygon points="0,0 32,0 32,70" fill="var(--fold-shadow)"/>
      <polygon points="0,0 32,0 32,60" fill="var(--brand-blue)"/>
    </svg>
    <ul class="contact">
      <li>5820 Birchmont Road</li>
      <li>Fallowby, FB 482917</li>
      <li><svg viewBox="0 0 14 12"><path d="M1 4 Q7 -1 13 4 L11 5 9 3 H5 L3 5Z M3 6 H11 L12 11 H2Z"/></svg>555-318-2746 x 100</li>
      <li><svg viewBox="0 0 14 12"><path d="M1 4 Q7 -1 13 4 L11 5 9 3 H5 L3 5Z M3 6 H11 L12 11 H2Z"/></svg>555-318-2746 Toll Free</li>
      <li><svg viewBox="0 0 14 12"><path d="M4 0 H10 V4 H4Z M1 5 H13 V11 H1Z M3 7 V9 H11 V7Z" fill-rule="evenodd"/></svg>555-902-6613</li>
      <li><svg viewBox="0 0 14 12"><path d="M1 2 H13 V11 H1Z M2.5 3.5 L7 7 L11.5 3.5 V9.5 H2.5Z" fill-rule="evenodd"/></svg>name@varodine.example</li>
      <li><svg viewBox="0 0 14 12"><circle cx="7" cy="6" r="5.5"/><path d="M1.5 6 H12.5 M7 0.5 V11.5" stroke="#fff" stroke-width="1"/></svg>www.varodine.example</li>
    </ul>
  </section>

</div>
</body>
</html>
```